QM Fenwold Detailing, Inc.

I'm looking for business card design for an existing company with an existing logo/website. www.qmfenwold-detailing.com. VETERAN OWNED logo must be present.

Target Market(s)

Structural and architectural steel fabricators

Industry/Entity Type

Structural and architectural steel detailing and engineering

Contact Information for Business Card

logo, business name, address, phone, website, email, employee info

Font styles to use
Serif

Colors
00AB8E
00BBA5
67D7C9
C6EFE9
E9F9F6

Requirements
Must have
• company logo, website, VETERAN OWNED LOGO
Should not have
• Don't make it too busy. Less is more

```html
<!DOCTYPE html>
<html lang="en">
<head>
<meta charset="utf-8">
<title>QM Fenwold Detailing, Inc. – Business Card</title>
<link href="https://fonts.googleapis.com/css2?family=Poppins:wght@300;400;500;600&display=swap" rel="stylesheet">
<style>
  :root {
    --page: #2b2c2e;
    --card: #1e1f21;
    --card-edge: #26272a;
    --teal: #3cc8cf;
    --teal-deep: #1f8f96;
    --text-grey: #a9acb0;
    --text-soft: #7d8084;
    --rule: #2a9aa1;
    --badge-red: #d5202a;
    --badge-blue: #1d4f9c;
  }
  * { box-sizing: border-box; margin: 0; padding: 0; }
  html, body {
    width: 1200px; height: 1108px; overflow: hidden;
    background: var(--page);
    font-family: "Poppins", sans-serif;
  }
  .stage {
    position: relative; width: 1200px; height: 1108px;
  }
  .card {
    position: absolute; top: 150px;
    width: 470px; height: 808px;
    background: var(--card);
    border-radius: 26px;
    box-shadow: 0 18px 40px rgba(0,0,0,.45);
    overflow: hidden;
  }
  .card--front { left: 85px; }
  .card--back { left: 645px; }

  /* Front */
  .wordmark {
    position: absolute; top: 170px; left: 0; right: 0;
    text-align: center;
    color: var(--teal);
    font-weight: 500;
    font-size: 40px;
    line-height: 1.15;
    letter-spacing: 1px;
  }
  .person {
    position: absolute; top: 430px; left: 0; right: 0; text-align: center;
  }
  .person__name {
    color: var(--teal); font-weight: 600; font-size: 30px; letter-spacing: 1.5px;
  }
  .person__title {
    color: var(--text-grey); font-weight: 400; font-size: 17px; letter-spacing: 2px; margin-top: -4px;
  }
  .icon-row {
    position: absolute; top: 530px; left: 50px; right: 50px;
    display: flex; align-items: center; gap: 10px;
  }
  .icon-row__rule { flex: 1; height: 1px; background: var(--rule); }
  .icon-box {
    width: 30px; height: 30px; border-radius: 4px;
    background: var(--teal-deep);
    display: flex; align-items: center; justify-content: center;
  }
  .icon-box svg { width: 18px; height: 18px; fill: #e9f9f6; }
  .contact {
    position: absolute; top: 578px; left: 0; right: 0; text-align: center;
    color: var(--text-grey); font-size: 17px; line-height: 1.55;
  }
  .contact__web-accent { color: var(--teal); }
  .divider {
    position: absolute; top: 680px; left: 70px; right: 70px; height: 1px; background: var(--rule);
  }
  .address {
    position: absolute; top: 694px; left: 0; right: 0; text-align: center;
    color: var(--text-grey); font-size: 17px; line-height: 1.5;
  }

  /* Back */
  .back-texture {
    position: absolute; inset: 0;
    background: linear-gradient(200deg, #5a5c60 0%, #35373a 30%, #1c1d1f 60%, #141516 100%);
  }
  .back-mark {
    position: absolute; top: 440px; left: 0; right: 0; text-align: center;
    color: var(--teal); font-weight: 500; font-size: 26px; letter-spacing: 1px;
  }
  .veteran-badge {
    position: absolute; top: 640px; left: 170px;
    width: 120px; height: 120px; border-radius: 50%;
    background: linear-gradient(135deg, var(--badge-blue) 0%, var(--badge-red) 100%);
  }
</style>
</head>
<body>
<main class="stage">
  <section class="card card--front" aria-label="Card front">
    <div class="wordmark">QM Fenwold<br>Detailing</div>

    <div class="person">
      <p class="person__name">DANIEL HARROW</p>
      <p class="person__title">MANAGING DIRECTOR</p>
    </div>

    <div class="icon-row">
      <span class="icon-row__rule"></span>
      <span class="icon-box" aria-label="Phone">
        <svg viewBox="0 0 24 24"><path d="M6.6 10.8a15 15 0 0 0 6.6 6.6l2.2-2.2a1 1 0 0 1 1-.25 11.4 11.4 0 0 0 3.6.57 1 1 0 0 1 1 1V20a1 1 0 0 1-1 1A17 17 0 0 1 3 4a1 1 0 0 1 1-1h3.5a1 1 0 0 1 1 1c0 1.25.2 2.45.57 3.57a1 1 0 0 1-.25 1z"/></svg>
      </span>
      <span class="icon-box" aria-label="Email">
        <svg viewBox="0 0 24 24"><path d="M3 5h18v14H3zm2 2v.3l7 4.7 7-4.7V7zm0 2.7V17h14V9.7l-7 4.6z"/></svg>
      </span>
      <span class="icon-box" aria-label="Website">
        <svg viewBox="0 0 24 24"><path d="M12 2a10 10 0 1 0 0 20 10 10 0 0 0 0-20zm0 2a8 8 0 0 1 7.7 6h-3.3a14 14 0 0 0-2-5.6A8 8 0 0 1 12 4zm-2.4.4A14 14 0 0 0 7.6 10H4.3A8 8 0 0 1 9.6 4.4zM4.3 12h3.2a14 14 0 0 0 2.1 7.6A8 8 0 0 1 4.3 12zm10.1 7.6a14 14 0 0 0 2.1-7.6h3.2a8 8 0 0 1-5.3 7.6zM9.6 12h4.8a12 12 0 0 1-2.4 7 12 12 0 0 1-2.4-7zm0-2A12 12 0 0 1 12 5a12 12 0 0 1 2.4 5z"/></svg>
      </span>
      <span class="icon-row__rule"></span>
    </div>

    <div class="contact">
      <p>044-555 018 642</p>
      <p>info@qmfenwold-detailing.com</p>
      <p>www.<span class="contact__web-accent">qmfenwold-detailing</span>.com</p>
    </div>

    <div class="divider"></div>

    <div class="address">
      <p>421, Address line goes here</p>
      <p>45452, Country Name</p>
    </div>
  </section>

  <section class="card card--back" aria-label="Card back">
    <div class="back-texture" role="img" aria-label="Repeating tonal company-mark pattern in glossy black and grey"></div>
    <p class="back-mark">QM Fenwold</p>
    <div class="veteran-badge" role="img" aria-label="Veteran owned business badge"></div>
  </section>
</main>
</body>
</html>
```